Building Company Business Card Design

Need a design for a business card:
It needs to have: Name, Phone, Facebook link, Website, email
i would also like a list of works we undertake:
-New Homes
-Extensions, Renovations & Bathrooms
-Decking, Carports, Sheds (Residential and Industrial)
-Carpentry
-Fences, Patios & Pergolas

Name, Phone, Facebook link, Website, email + details of services provided listed in description

```html
<!DOCTYPE html>
<html lang="en">
<head>
<meta charset="utf-8">
<title>Summit Ridge Builders – Business Card</title>
<link href="https://fonts.googleapis.com/css2?family=Montserrat:wght@400;500;700;800&display=swap" rel="stylesheet">
<style>
  :root {
    --stage: #222222;
    --green: #2fb34a;
    --green-deep: #27a843;
    --white: #ffffff;
    --ink: #1d1d1d;
    --ink-soft: #4a4a4a;
    --grey: #8a8a8a;
    --social: #3b5aa0;
  }
  * { box-sizing: border-box; margin: 0; padding: 0; }
  html, body { width: 1200px; height: 711px; overflow: hidden; background: var(--stage); }
  body { font-family: "Montserrat", sans-serif; position: relative; }

  .card { position: absolute; border-radius: 26px; overflow: hidden; }

  /* ---------- Services side (landscape) ---------- */
  .card-services {
    left: 50px; top: 185px; width: 600px; height: 345px;
    background: var(--green);
    display: flex; padding: 38px 34px 38px 40px; gap: 28px;
  }
  .brand-block { width: 250px; display: flex; flex-direction: column; justify-content: center; }
  .brand-mark { display: flex; align-items: center; gap: 10px; }
  .brand-square { width: 18px; height: 18px; background: var(--ink); flex: none; }
  .brand-name {
    font-weight: 800; font-size: 38px; line-height: 1.02; color: var(--ink);
    letter-spacing: 0.5px;
  }
  .brand-sub {
    margin-top: 8px; font-weight: 500; font-size: 13px; letter-spacing: 2.4px;
    color: var(--ink);
  }
  .service-list { list-style: none; flex: 1; display: flex; flex-direction: column; justify-content: center; gap: 16px; }
  .service-list li {
    color: var(--white); font-size: 15px; font-weight: 500; line-height: 1.3;
    padding-left: 22px; position: relative;
  }
  .service-list li::before {
    content: ""; position: absolute; left: 0; top: 5px;
    width: 10px; height: 10px; border-radius: 50%; background: var(--white);
  }

  /* ---------- Contact side (portrait) ---------- */
  .card-contact {
    left: 760px; top: 70px; width: 345px; height: 580px;
    background: var(--green-deep);
  }
  .contact-head { position: absolute; inset: 0; }
  .contact-brand {
    position: absolute; left: 30px; top: 38px; right: 26px;
    display: flex; align-items: center; gap: 10px;
  }
  .contact-brand .brand-square { width: 14px; height: 14px; background: var(--green); }
  .contact-brand .brand-name { font-size: 26px; color: var(--ink); }
  .contact-brand-sub {
    position: absolute; left: 54px; top: 72px;
    font-size: 10.5px; font-weight: 500; letter-spacing: 1.6px; color: var(--grey);
  }
  .mark-space {
    position: absolute; left: 50%; top: 150px; transform: translateX(-50%);
    width: 120px; height: 120px; background: var(--white);
  }
  .person { position: absolute; left: 0; right: 0; top: 300px; text-align: center; color: var(--white); }
  .person-name { font-weight: 800; font-size: 22px; letter-spacing: 0.5px; }
  .person-role { font-size: 15px; margin-top: 2px; }
  .icon-row { position: absolute; left: 0; right: 0; top: 370px; display: flex; justify-content: center; gap: 18px; }
  .icon { width: 26px; height: 26px; border-radius: 50%; background: var(--white); display: flex; align-items: center; justify-content: center; }
  .icon.social { background: var(--social); }
  .contact-lines { position: absolute; left: 0; right: 0; top: 412px; text-align: center; color: var(--white); font-size: 13.5px; line-height: 1.45; }
  .divider { position: absolute; left: 50px; right: 50px; top: 498px; height: 1px; background: var(--white); opacity: 0.85; }
  .address { position: absolute; left: 0; right: 0; top: 510px; text-align: center; color: var(--white); font-size: 14px; line-height: 1.4; }
</style>
</head>
<body>

  <section class="card card-services">
    <div class="brand-block">
      <div class="brand-mark">
        <span class="brand-square"></span>
        <span class="brand-name">SUMMIT<br>RIDGE</span>
      </div>
      <div class="brand-sub">BUILDERS PTY LTD</div>
    </div>
    <ul class="service-list">
      <li>New Homes</li>
      <li>Extensions, Renovations &amp; Bathrooms</li>
      <li>Decking, Carports, Sheds (Residential and Industrial)</li>
      <li>Carpentry</li>
      <li>Fences, Patios &amp; Pergolas</li>
    </ul>
  </section>

  <section class="card card-contact">
    <svg class="contact-head" width="345" height="580" viewBox="0 0 345 580" aria-hidden="true">
      <polygon points="0,0 345,0 345,105 0,235" fill="var(--white)"/>
    </svg>
    <div class="contact-brand">
      <span class="brand-square"></span>
      <span class="brand-name">SUMMIT RIDGE</span>
    </div>
    <div class="contact-brand-sub">BUILDERS PTY LTD</div>

    <div class="person">
      <div class="person-name">DANIEL CARTER</div>
      <div class="person-role">Co-Founder &amp; CEO</div>
    </div>

    <div class="icon-row">
      <span class="icon social"></span>
      <span class="icon">
        <svg width="14" height="14" viewBox="0 0 24 24"><path d="M6.6 10.8a15 15 0 0 0 6.6 6.6l2.2-2.2c.3-.3.7-.4 1-.2 1.1.4 2.3.6 3.6.6.6 0 1 .4 1 1V20c0 .6-.4 1-1 1A17 17 0 0 1 3 4c0-.6.4-1 1-1h3.5c.6 0 1 .4 1 1 0 1.3.2 2.5.6 3.6.1.3 0 .7-.2 1z" fill="var(--green-deep)"/></svg>
      </span>
      <span class="icon">
        <svg width="15" height="12" viewBox="0 0 24 18"><rect x="1" y="1" width="22" height="16" rx="2" fill="none" stroke="var(--green-deep)" stroke-width="2.2"/><path d="M1 2l11 8 11-8" fill="none" stroke="var(--green-deep)" stroke-width="2.2"/></svg>
      </span>
      <span class="icon">
        <svg width="15" height="15" viewBox="0 0 24 24"><circle cx="12" cy="12" r="10" fill="none" stroke="var(--green-deep)" stroke-width="2"/><ellipse cx="12" cy="12" rx="4.5" ry="10" fill="none" stroke="var(--green-deep)" stroke-width="2"/><path d="M2 12h20" stroke="var(--green-deep)" stroke-width="2"/></svg>
      </span>
    </div>

    <div class="contact-lines">
      555-0142-38610<br>
      hello@summitridge-mail.com<br>
      @summitridge-social.com<br>
      www.summitridge-web.com
    </div>
    <div class="divider"></div>
    <div class="address">
      18 Harbor Mill Lane<br>
      Fairhaven, CT 06000 USA
    </div>
  </section>

</body>
</html>
```